New Update: I am changing the title of the book and the back cover text. Title was too long before. Same style as before.
New Title: Standing Again
New Subtitle: One Family’s Road Back to Wholeness (italics on front cover)

Back cover text:
Standing Again: One Family’s Road Back to Wholeness offers clear, compassionate guidance for those recovering from total loss. Drawing from his experience as a Carrow Storm survivor, Tobias Lindqvell shares practical advice on insurance, rebuilding, and emotional healing, along with lessons in strength and community. This is not a book about tragedy; it’s about perseverance and renewal. Standing Again is a trusted companion for anyone rebuilding life, home, and hope after disaster.

Font styles to use
Serif

Colors
EB3D1F
EC4F4E
F09395
F8D3D4
FCEDEE

Requirements
Should not have
• No pictures or anything related to fire on the cover.

```html
<!DOCTYPE html>
<html lang="en">
<head>
<meta charset="utf-8">
<title>Standing Again – Cover Wrap</title>
<link rel="stylesheet" href="https://fonts.googleapis.com/css2?family=Stint+Ultra+Condensed&family=Cormorant+Garamond:ital,wght@1,600&family=Oswald:wght@300;400;500&family=Archivo:ital,wght@1,800&display=swap">
<style>
  :root {
    --red: #EB3D1F;
    --coral: #EC4F4E;
    --rose: #F09395;
    --blush: #F8D3D4;
    --shell: #FCEDEE;
    --stage: #EFE8E6;
    --cover-h: 720px;
    --cover-w: 430px;
    --spine-w: 26px;
  }
  * { box-sizing: border-box; margin: 0; padding: 0; }
  html, body {
    width: 1200px; height: 800px; overflow: hidden;
    background: var(--stage);
  }
  .wrap {
    position: absolute;
    top: 40px;
    left: calc((1200px - (var(--cover-w) * 2 + var(--spine-w))) / 2);
    display: flex;
    height: var(--cover-h);
    box-shadow: 0 10px 30px rgba(90, 40, 40, 0.18);
  }
  .panel {
    position: relative;
    width: var(--cover-w);
    height: 100%;
    background: linear-gradient(180deg, var(--shell) 0%, var(--blush) 45%, var(--rose) 82%, #E0696C 100%);
    overflow: hidden;
  }

  /* Back cover */
  .author-photo {
    position: absolute;
    top: 150px; right: 0;
    width: 140px; height: 180px;
    background: linear-gradient(180deg, rgba(120,110,110,0.55) 0%, rgba(40,50,80,0.7) 55%, rgba(248,211,212,0) 100%);
  }
  .back-author {
    position: absolute;
    top: 345px; right: 0; left: 0;
    text-align: right;
    padding-right: 22px;
    font-family: "Oswald", sans-serif;
    font-weight: 400;
    font-size: 34px;
    color: var(--red);
    letter-spacing: -0.5px;
  }
  .blurb {
    position: absolute;
    top: 420px; left: 36px; right: 30px;
    text-align: center;
    font-family: "Oswald", sans-serif;
    font-weight: 300;
    font-size: 14.5px;
    line-height: 1.55;
    color: var(--red);
  }
  .blurb .lead { display: block; }

  /* Spine */
  .spine {
    position: relative;
    width: var(--spine-w);
    height: 100%;
    background: linear-gradient(180deg, #F3C3C4 0%, #EDB0B2 50%, #D9676A 100%);
  }
  .spine-title {
    position: absolute;
    left: 50%; top: 50%;
    transform: translate(-50%, -50%) rotate(-90deg);
    white-space: nowrap;
    font-family: "Archivo", sans-serif;
    font-style: italic;
    font-weight: 800;
    font-size: 13px;
    letter-spacing: 1.5px;
    color: var(--red);
    text-transform: uppercase;
  }

  /* Front cover */
  .title {
    position: absolute;
    top: 52px; left: 0; right: 0;
    text-align: center;
    font-family: "Stint Ultra Condensed", serif;
    font-weight: 400;
    color: var(--red);
    text-transform: uppercase;
    line-height: 0.88;
  }
  .title-line { display: block; font-size: 118px; }
  .house-art {
    position: absolute;
    top: 300px; left: 105px;
    width: 220px; height: 170px;
    background: linear-gradient(180deg, rgba(236,154,156,0.85) 0%, rgba(242,179,181,0.5) 60%, rgba(248,211,212,0) 100%);
  }
  .subtitle {
    position: absolute;
    top: 505px; left: 0; right: 0;
    text-align: center;
    font-family: "Cormorant Garamond", serif;
    font-style: italic;
    font-weight: 600;
    color: var(--red);
    line-height: 1.05;
  }
  .subtitle-small { display: block; font-size: 27px; font-variant: small-caps; }
  .subtitle-large { display: block; font-size: 36px; text-transform: uppercase; letter-spacing: 0.5px; }
  .front-author {
    position: absolute;
    bottom: 36px; left: 0; right: 0;
    text-align: center;
    font-family: "Oswald", sans-serif;
    font-weight: 500;
    font-size: 54px;
    color: var(--blush);
    letter-spacing: -0.5px;
  }
</style>
</head>
<body>
  <div class="wrap">
    <section class="panel back-cover">
      <div class="author-photo" role="img" aria-label="Portrait photograph of the author"></div>
      <h2 class="back-author">Tobias Lindqvell</h2>
      <p class="blurb">
        <span class="lead">Standing Again:</span>
        One Family’s Road Back to Wholeness offers clear, compassionate guidance for those recovering from total loss. Drawing from his experience as a Carrow Storm survivor, Tobias Lindqvell shares practical advice on insurance, rebuilding, and emotional healing, along with lessons in strength and community. This is not a book about tragedy; it’s about perseverance and renewal. Standing Again is a trusted companion for anyone rebuilding life, home, and hope after disaster.
      </p>
    </section>

    <div class="spine">
      <span class="spine-title">Standing Again: One Family’s Road Back to Wholeness</span>
    </div>

    <section class="panel front-cover">
      <h1 class="title">
        <span class="title-line">Standing</span>
        <span class="title-line">Again</span>
      </h1>
      <div class="house-art" role="img" aria-label="Faded illustration of a simple house with a round attic window"></div>
      <p class="subtitle">
        <span class="subtitle-small">One Family’s Road</span>
        <span class="subtitle-large">Back to Wholeness</span>
      </p>
      <p class="front-author">Tobias Lindqvell</p>
    </section>
  </div>
</body>
</html>
```